Hop Grower Producer Card

A wisconsin based grower of high quality mid westrn grown Hops with the concept of growing and processing Hops into pellet form for sale to brewers of beer large and small .varieties are grown are Cascade ,Chinook and Centennial

Target Market(s)

Brew masters at micro brews and large breweries

Industry/Entity Type

Processing

Font styles to use
Decorative
Script

Requirements
Must have
• i would like the Hop varieties listed on the back of the card , with the statement Grower of High Quality Wisconsin Hops and the web site address
Nice to have
• german style font for the name Volmer's Bine Lodge

```html
<!DOCTYPE html>
<html lang="en">
<head>
<meta charset="utf-8">
<title>Volmer's Bine Lodge – Business Card</title>
<link href="https://fonts.googleapis.com/css2?family=UnifrakturCook:wght@700&family=Uncial+Antiqua&family=Berkshire+Swash&family=Ubuntu:wght@400&family=Lora:wght@700&display=swap" rel="stylesheet">
<style>
  :root {
    --page-bg: #e6e2db;
    --front-black: #050805;
    --front-green-glow: #1f4a22;
    --leaf-light: #b3dd86;
    --leaf-mid: #74ac4a;
    --leaf-bright: #9fd35a;
    --muted-grey: #c9c9c9;
    --ink-black: #0c0c0c;
    --back-white: #ffffff;
    --back-green: #2f7a2f;
    --back-dark-green: #24552a;
  }
  * { margin: 0; padding: 0; box-sizing: border-box; }
  html, body { width: 900px; height: 1200px; overflow: hidden; }
  body { background: var(--page-bg); position: relative; font-family: "Ubuntu", sans-serif; }

  .card { position: absolute; left: 32px; width: 840px; height: 492px; overflow: hidden; }
  .card--front {
    top: 83px;
    background: radial-gradient(ellipse at 45% 55%, var(--front-green-glow) 0%, var(--front-black) 55%),
                linear-gradient(90deg, var(--front-black) 40%, #14301a 100%);
  }
  .card--back { top: 621px; background: var(--back-white); }

  .brand-name {
    position: absolute; left: 0; width: 100%; text-align: center;
    font-family: "UnifrakturCook", serif; font-weight: 700; font-size: 74px; line-height: 1;
    letter-spacing: 1px;
  }
  .card--front .brand-name { top: 22px; color: var(--leaf-light); }
  .card--back .brand-name { top: 30px; color: var(--ink-black); }

  .tagline {
    position: absolute; left: 0; width: 100%; text-align: center;
    font-family: "Uncial Antiqua", serif; font-size: 31px; line-height: 1;
  }
  .card--front .tagline { top: 136px; color: var(--leaf-mid); }
  .card--back .tagline { top: 138px; color: var(--back-green); }

  .product-photo {
    position: absolute; left: 0; top: 170px; width: 540px; height: 322px;
    background: radial-gradient(ellipse at 50% 55%, #5e3d16 0%, #2a2210 40%, rgba(5,8,5,0) 75%),
                linear-gradient(180deg, rgba(5,8,5,0) 0%, #3a2a14 100%);
  }

  .contact { position: absolute; right: 36px; top: 198px; width: 270px; text-align: right; }
  .contact__name {
    font-family: "Berkshire Swash", cursive; font-size: 33px; color: var(--leaf-bright); line-height: 1.1;
  }
  .contact__role { font-size: 22px; color: var(--muted-grey); margin-top: 4px; }
  .contact__rule { height: 1px; background: var(--leaf-mid); margin: 10px 0 8px; }
  .contact__line { font-size: 19px; color: var(--leaf-light); line-height: 29px; }
  .contact__gap { height: 6px; }

  .hop-photo {
    position: absolute; left: 0; top: 170px; width: 840px; height: 322px;
    background: radial-gradient(ellipse at 45% 70%, #a9c97a 0%, #6f9a48 35%, rgba(150,180,120,0.6) 60%, rgba(255,255,255,0) 85%),
                linear-gradient(180deg, #ffffff 0%, #e4ecdd 40%, #b9cca6 100%);
  }
  .varieties {
    position: absolute; left: 0; width: 100%; top: 186px; text-align: center;
    font-family: "Uncial Antiqua", serif; font-size: 27px; color: var(--back-dark-green);
  }
  .website {
    position: absolute; left: 0; width: 100%; top: 230px; text-align: center;
    font-family: "Lora", serif; font-weight: 700; font-size: 23px; color: var(--back-dark-green);
  }
</style>
</head>
<body>
  <section class="card card--front">
    <div class="product-photo" role="img" aria-label="Photo of an oak barrel, hop cones, glasses of golden beer and a bottle on a wooden table"></div>
    <h1 class="brand-name">Volmer's Bine Lodge</h1>
    <p class="tagline">Grower Of High Quality Wisconsin Hops</p>
    <div class="contact">
      <p class="contact__name">Karl Volmer</p>
      <p class="contact__role">Owner /Manager</p>
      <div class="contact__rule"></div>
      <p class="contact__line">1427 Orchard Lane</p>
      <p class="contact__line">Merrill,WI54452</p>
      <div class="contact__gap"></div>
      <p class="contact__line">Cell : 715-555-0142</p>
      <p class="contact__line">Fax : 715-555-0187</p>
      <div class="contact__rule"></div>
      <p class="contact__line">binelodge7@mailbox.com</p>
      <p class="contact__line">www.binelodge7.com</p>
    </div>
  </section>

  <section class="card card--back">
    <div class="hop-photo" role="img" aria-label="Photo of green hop cones hanging on a leafy bine against a soft bright background"></div>
    <h2 class="brand-name">Volmer's Bine Lodge</h2>
    <p class="tagline">Grower Of High Quality Wisconsin Hops</p>
    <p class="varieties">Cascade,Chinook,Centennial</p>
    <p class="website">www.binelodge7.com</p>
  </section>
</body>
</html>
```